Schriftdesign für Shop-Header Bild (Schmuckhandel) / Online-Marketing Material
Zielgruppe
Wir verkaufen Schmuck im Onlineshop mit Herz
Aufgabenstellung
Wir benötigen den vorgegebenen Text in schöner Form, Farbe und Größe harmonisch eingefügt, in unserem Bild.
Folgender Text soll sich schick ins Bild einfügen oder in 3-D vielleicht in Schriftfarbe gold hervorheben:
Mit ganzem Herzen für Sie da!
Ihr Online -Juwelier mit Herz
Siehe auch unser altes Bild mit Text, im Shop, wie es nicht aussehen sollte: www.lindenglanzhof.de

```html
<!DOCTYPE html>
<html lang="de">
<head>
<meta charset="utf-8">
<title>Lindenglanzhof – Ihr Online-Juwelier mit Herz</title>
<link href="https://fonts.googleapis.com/css2?family=Didact+Gothic&family=Courier+Prime:ital,wght@1,700&family=Old+Standard+TT:wght@700&display=swap" rel="stylesheet">
<style>
  :root {
    --white: #ffffff;
    --red: #d9262b;
    --text-dark: #2b2b2b;
    --field-grey: #efefef;
    --nav-grey: #6b6566;
    --base-grey: #c9c7c6;
    --wood-dark: #4b433e;
    --wood-mid: #7d746d;
    --wood-light: #958b83;
    --gold-light: #fff3a6;
    --gold: #e2c13f;
    --gold-deep: #9c7a12;
  }
  * { margin: 0; padding: 0; box-sizing: border-box; }
  html, body { width: 1200px; height: 569px; overflow: hidden; background: var(--white); }
  body { position: relative; font-family: "Didact Gothic", Arial, sans-serif; color: var(--text-dark); }

  .site-header { position: absolute; inset: 0 0 auto 0; height: 126px; background: var(--white); }

  .brand {
    position: absolute; left: 112px; top: 48px;
    font-size: 24px; color: var(--red); letter-spacing: 0.5px;
  }

  .service-links {
    position: absolute; right: 113px; top: 10px;
    display: flex; gap: 19px; list-style: none; font-size: 11px;
  }
  .service-links .is-active { color: var(--red); }

  .search-label {
    position: absolute; left: 379px; top: 33px; font-size: 15px; color: var(--text-dark);
  }
  .search-label svg { vertical-align: middle; margin-left: 6px; }

  .search-field {
    position: absolute; left: 379px; top: 59px; width: 411px; height: 35px;
    background: var(--field-grey); color: var(--red); font-size: 12px;
    padding: 11px 23px;
  }
  .search-field svg { position: absolute; right: 8px; top: 5px; }

  .cart {
    position: absolute; left: 847px; top: 59px; width: 240px; height: 35px;
    background: var(--field-grey); color: var(--red); font-size: 12px;
    padding: 11px 23px;
  }
  .cart svg { position: absolute; right: 20px; top: 7px; }

  .main-nav {
    position: absolute; left: 0; top: 126px; width: 1200px; height: 39px;
    background: var(--nav-grey);
  }
  .main-nav .notch { position: absolute; left: 175px; top: 0; }
  .main-nav ul { list-style: none; }
  .main-nav li {
    position: absolute; top: 11px; color: var(--white);
    font-size: 16px; text-transform: uppercase; letter-spacing: 0.3px;
  }

  .hero {
    position: absolute; left: 0; top: 165px; width: 1200px; height: 345px;
    background:
      radial-gradient(ellipse 260px 220px at 250px 170px, rgba(168, 40, 42, 0.55), transparent 75%),
      linear-gradient(180deg, var(--wood-mid) 0%, var(--wood-light) 45%, var(--wood-dark) 100%);
  }

  .hero-title {
    position: absolute; left: 483px; top: 61px; width: 660px;
    font-family: "Old Standard TT", Georgia, serif; font-weight: 700;
    font-size: 34px; letter-spacing: 1.5px; white-space: nowrap;
    background: linear-gradient(180deg, var(--gold-light) 10%, var(--gold) 50%, var(--gold-deep) 95%);
    -webkit-background-clip: text; background-clip: text; color: transparent;
    filter: drop-shadow(2px 3px 2px rgba(0, 0, 0, 0.75));
  }

  .hero-rule {
    position: absolute; left: 487px; top: 129px; width: 713px; height: 2px;
    background: linear-gradient(90deg, rgba(226, 193, 63, 0.2), var(--gold) 20%, var(--gold) 70%, rgba(226, 193, 63, 0.3));
  }

  .hero-tagline {
    position: absolute; left: 615px; top: 155px; white-space: nowrap;
    font-family: "Courier Prime", "Courier New", monospace; font-style: italic; font-weight: 700;
    font-size: 27px;
    background: linear-gradient(180deg, var(--gold-light) 10%, var(--gold) 55%, var(--gold-deep) 95%);
    -webkit-background-clip: text; background-clip: text; color: transparent;
    filter: drop-shadow(2px 2px 2px rgba(0, 0, 0, 0.75));
  }

  .hero-base {
    position: absolute; left: 0; top: 510px; width: 1200px; height: 20px;
    background: linear-gradient(180deg, var(--base-grey), var(--white));
  }
</style>
</head>
<body>
  <header class="site-header">
    <div class="brand">Lindenglanzhof</div>

    <ul class="service-links">
      <li class="is-active">Startseite</li>
      <li>Anmelden</li>
      <li>Mein Konto</li>
      <li>Newsletter abonnieren</li>
      <li>Kontakt</li>
    </ul>

    <div class="search-label">Nach welchem Artikel suchen Sie?
      <svg width="12" height="7" viewBox="0 0 12 7" aria-hidden="true"><polygon points="0,0 12,0 6,7" fill="#d9262b"/></svg>
    </div>

    <div class="search-field">Suchen nach
      <svg width="26" height="24" viewBox="0 0 26 24" aria-hidden="true">
        <rect width="26" height="24" rx="5" fill="#d9262b"/>
        <circle cx="12" cy="11" r="5" fill="none" stroke="#fff" stroke-width="2"/>
        <line x1="15.5" y1="14.5" x2="19" y2="18" stroke="#fff" stroke-width="2.4" stroke-linecap="round"/>
      </svg>
    </div>

    <div class="cart">Ihr Warenkorb ist leer.
      <svg width="20" height="22" viewBox="0 0 20 22" aria-hidden="true">
        <path d="M6 6 V4 a4 4 0 0 1 8 0 V6" fill="none" stroke="#d9262b" stroke-width="2"/>
        <rect x="0" y="6" width="20" height="16" rx="2" fill="#d9262b"/>
      </svg>
    </div>
  </header>

  <nav class="main-nav">
    <svg class="notch" width="48" height="22" viewBox="0 0 48 22" aria-hidden="true"><polygon points="0,0 48,0 24,22" fill="#ffffff"/></svg>
    <ul>
      <li style="left:252px">Kreuz-Anhänger</li>
      <li style="left:437px">Anhänger/Versch.</li>
      <li style="left:637px">Foto-Medaillons</li>
      <li style="left:824px">Ohrschmuck</li>
      <li style="left:974px">Accessoires</li>
    </ul>
  </nav>

  <section class="hero" role="img" aria-label="Foto: rotes Holzherz mit Schlüsselloch, ein Schlüssel und ein roter Herzrahmen an roter Kordel auf dunkler Holzmaserung">
    <h1 class="hero-title">MIT GANZEM HERZEN FÜR SIE DA!</h1>
    <div class="hero-rule"></div>
    <p class="hero-tagline">Ihr Online-Juwelier mit Herz</p>
  </section>

  <div class="hero-base"></div>
</body>
</html>
```